Complete Stationary Package for Sea Harvest Trading Company
Silver Lantern Sea Harvest 銀燈海珍
Complete Stationary Package for Sea Harvest Trading Company - Food
Creative Brief
Simple
Malcolm Whitby 马尔
Director of Sales and Distribution
Silver Lantern Sea Harvest, Level 11, KL Plaza 5, Jalan Kenari Raya, Bangsar, 59100 Kuala Lumpur, Malaysia
mwhitby@slseaharvest-example.com
www.slseaharvest-example.com
We need a full stationary package design - business cards, letterhead, envelopes, folders, invoice, email signature and any other standard stationary items you may decide to include in your concepts. I need the text below written in smaller print somewhere on the card either on the front or the back " Silver Lantern Sea Harvest is a registered trademark of Corvale Holdings Sdn Bhd 8827165K". I like the same cream colour that is used in the packaging that I have uploaded. I do not want the card to have a white background colour. I would like red and/or gold to feature also.
I would like a suitable design for the back of the card with the company name and logo.

```html
<!DOCTYPE html>
<html lang="en">
<head>
<meta charset="utf-8">
<title>Silver Lantern Sea Harvest — Business Card</title>
<link rel="stylesheet" href="https://fonts.googleapis.com/css2?family=Cormorant+Garamond:wght@500;600&family=Noto+Serif+TC:wght@500&display=swap">
<style>
  :root {
    --backdrop: #4a4239;
    --cream: #f3ead8;
    --gold-light: #e6c65a;
    --gold: #c9a22c;
    --gold-deep: #9c7a17;
    --gold-text: #b08a2a;
    --ink: #6b5c45;
    --red: #b3242c;
    --white: #ffffff;
  }
  * { margin: 0; padding: 0; box-sizing: border-box; }
  html, body {
    width: 1200px; height: 904px; overflow: hidden;
    background: var(--backdrop);
    font-family: "Cormorant Garamond", "Noto Serif TC", serif;
  }
  .card {
    position: absolute; left: 250px;
    width: 700px; height: 400px;
    border-radius: 0 200px 200px 0;
    overflow: hidden;
  }
  .card--back { top: 32px; }
  .card--front { top: 472px; background: var(--cream); }

  .back-pattern {
    position: absolute; inset: 0;
    background: radial-gradient(circle at 60% 45%, var(--gold-light), var(--gold) 55%, var(--gold-deep));
  }
  .back-mark {
    position: absolute; right: 110px; top: 110px;
    width: 180px; height: 180px; border-radius: 50%;
    background: var(--white);
    display: flex; align-items: center; justify-content: center;
    text-align: center; padding: 20px;
    color: var(--gold-deep); font-weight: 600;
    font-size: 20px; line-height: 1.15; letter-spacing: 0.5px;
  }

  .trademark-band {
    position: absolute; left: 0; top: 0; bottom: 0; width: 34px;
    background: var(--red);
  }
  .trademark-band span {
    position: absolute; left: 50%; top: 50%;
    width: 370px;
    transform: translate(-50%, -50%) rotate(-90deg);
    text-align: center;
    color: var(--cream); font-size: 10px; font-weight: 500;
    line-height: 1.2; letter-spacing: 0.2px;
  }

  .contact {
    position: absolute; left: 72px; top: 70px; width: 380px;
    color: var(--ink); font-size: 15px; line-height: 1.45; font-weight: 500;
  }
  .contact__name { color: var(--gold-text); font-size: 28px; font-weight: 600; line-height: 1.1; }
  .contact__title { color: var(--gold-text); font-size: 15px; margin-bottom: 16px; }
  .contact__company { font-weight: 600; }
  .contact__lines { margin-top: 14px; }
  .contact__lines p { display: flex; align-items: center; gap: 8px; }
  .contact__lines svg { width: 12px; height: 12px; flex: none; }

  .brand {
    position: absolute; right: 60px; top: 86px; width: 240px;
    display: flex; flex-direction: column; align-items: center; gap: 12px;
    color: var(--gold-text); font-weight: 600; text-align: center;
  }
  .brand__dot { width: 90px; height: 90px; border-radius: 50%; border: 3px solid var(--gold); }
  .brand__name { display: flex; flex-direction: column; align-items: center; gap: 4px; }
  .brand__name-zh { font-size: 24px; line-height: 1.2; letter-spacing: 2px; }
  .brand__name-en { font-size: 19px; line-height: 1.2; letter-spacing: 1.5px; white-space: nowrap; }
</style>
</head>
<body>

<section class="card card--back" aria-label="Business card back">
  <div class="back-pattern" role="img" aria-label="Embossed gold repeating brand pattern"></div>
  <div class="back-mark">Silver Lantern Sea Harvest</div>
</section>

<section class="card card--front" aria-label="Business card front">
  <div class="trademark-band">
    <span>Silver Lantern Sea Harvest is a registered trademark of<br>Corvale Holdings Sdn Bhd 8827165K</span>
  </div>

  <div class="contact">
    <h1 class="contact__name">Malcolm Whitby 马尔</h1>
    <p class="contact__title">Director of Sales and Distribution</p>
    <p class="contact__company">Silver Lantern Sea Harvest</p>
    <p>Level 11, KL Plaza 5, Jalan Kenari Raya,</p>
    <p>Bangsar, 59100 Kuala Lumpur, Malaysia</p>
    <div class="contact__lines">
      <p><svg viewBox="0 0 12 12"><path d="M2 1h3l1 3-1.5 1a6 6 0 0 0 2.5 2.5L8 6l3 1v3a1 1 0 0 1-1 1A9 9 0 0 1 1 2a1 1 0 0 1 1-1z" fill="var(--gold)"/></svg>T: +603 2100 4821</p>
      <p><svg viewBox="0 0 12 12"><rect x="1" y="3" width="10" height="7" fill="var(--gold)"/><rect x="3" y="1" width="6" height="3" fill="var(--gold)"/></svg>F: +603 2100 4822</p>
      <p><svg viewBox="0 0 12 12"><rect x="1" y="2.5" width="10" height="7" fill="none" stroke="var(--gold)" stroke-width="1.2"/><path d="M1 2.5l5 4 5-4" fill="none" stroke="var(--gold)" stroke-width="1.2"/></svg>mwhitby@slseaharvest-example.com</p>
      <p><svg viewBox="0 0 12 12"><circle cx="6" cy="6" r="5" fill="none" stroke="var(--gold)" stroke-width="1.2"/><path d="M1 6h10M6 1c-2.5 3-2.5 7 0 10M6 1c2.5 3 2.5 7 0 10" fill="none" stroke="var(--gold)" stroke-width="1"/></svg>www.slseaharvest-example.com</p>
    </div>
  </div>

  <div class="brand">
    <div class="brand__dot"></div>
    <div class="brand__name">
      <span class="brand__name-zh">銀燈海珍</span>
      <span class="brand__name-en">Silver Lantern</span>
      <span class="brand__name-en">Sea Harvest</span>
    </div>
  </div>
</section>

</body>
</html>
```